Driving-coach/trainer who wants to inform about the offer and how I can help people to drive more re

I need a flyer that informs potential customers about my offer.

DL size 210 mm x 99 mm, vertical!

I'm a trainer/coach who helps people to drive a car more relaxed, without fear and more confident.

It's a one to one training. I do train people in their own car. It gets people their freedom back to go where and when they like to go by own car...

Target Market(s)

People (man an woman) who are afraid of driving a car, or are very stressed while driving....

Industry/Entity Type

Life Coaching

Font styles to use
Sans Serif

Colors
acd136

Requirements
Must have
• Page 1:
• -my offer (see text-pdf)
• -three fotos (see attached files "Pixmarra") of people who are satisfied with my offer
• Page 2:
• -advantages in the work with me.
• -contact information
• -and a picture of me (see attached file) next to the contact information or the advantages of my work
• -my logo (see attached file) on Page 1 + 2
• -i like a "clear" and structured layout. "Less is more"

```html
<!DOCTYPE html>
<html lang="de">
<head>
<meta charset="utf-8">
<title>Flyer Fahrangst-Coaching</title>
<link href="https://fonts.googleapis.com/css2?family=Roboto+Condensed:wght@300;400;700&display=swap" rel="stylesheet">
<style>
  :root{
    --stage:#0e120e;
    --green:#7cb518;
    --green-bright:#a4d12a;
    --green-text:#79b316;
    --green-soft:#d2e79b;
    --bar:#c4e06a;
    --ink:#1f2a10;
    --grey:#e9e9ea;
    --white:#ffffff;
  }
  *{box-sizing:border-box;margin:0;padding:0}
  html,body{width:1200px;height:1200px;overflow:hidden;background:var(--stage)}
  body{font-family:"Roboto Condensed",Arial,sans-serif;position:relative;color:var(--ink)}
  .panel{position:absolute;top:116px;width:480px;height:986px;background:var(--white);overflow:hidden}
  .panel--front{left:94px}
  .panel--back{left:630px}
  .abs{position:absolute;left:0;width:100%}

  /* front */
  .front-title{top:0;height:54px;display:flex;align-items:center;justify-content:center;font-weight:700;font-size:31px;color:var(--green-text)}
  .front-photos{top:54px;height:168px}
  .intro{top:222px;height:118px;background:var(--green-soft);padding:33px 28px 0;font-weight:300;font-size:19px;line-height:31px;color:#222;white-space:nowrap}
  .cta{top:340px;height:68px;background:var(--green);display:flex;align-items:center;justify-content:center;color:var(--white);font-weight:700;font-size:30px;z-index:1}
  .cta::after{content:"";position:absolute;left:50%;bottom:-10px;margin-left:-14px;border-left:14px solid transparent;border-right:14px solid transparent;border-top:10px solid var(--green)}
  .question{top:408px;height:76px;padding:34px 28px 0;font-weight:300;font-size:19px;color:#222;background:var(--white);white-space:nowrap}
  .situations{top:484px;height:306px;background:var(--green);padding:38px 28px 0 30px;list-style:none}
  .situations li{border-left:3px solid var(--bar);padding-left:8px;font-size:12.5px;line-height:20.5px;font-weight:300;color:#1c2a08;margin-bottom:18px}
  .situations b{font-weight:700}
  .contact-head{top:790px;height:47px;display:flex;align-items:center;justify-content:center;font-weight:700;font-size:19px;color:var(--green-text)}
  .contact{top:837px;height:149px;background:var(--grey);text-align:center;font-size:16px;color:#222;padding-top:26px}
  .contact p{font-weight:300;line-height:23px}
  .contact strong{font-weight:700}
  .contact hr{border:0;border-top:1px solid #c8c8c8;width:350px;margin:10px auto 12px}

  /* back */
  .steps-band{top:0;height:124px;background:var(--green-bright)}
  .steps-title{position:absolute;top:40px;left:0;width:418px;height:45px;background:var(--white);border-radius:0 23px 23px 0;display:flex;align-items:center;padding-left:27px;gap:9px;font-weight:700;font-size:32px;color:var(--green-bright);box-shadow:0 3px 5px rgba(0,0,0,.15)}
  .steps-title .num{width:32px;height:32px;border-radius:50%;background:var(--green-bright);color:var(--white);font-size:23px;display:flex;align-items:center;justify-content:center}
  .scene{top:124px;height:438px}
  .step{position:absolute;top:127px;width:132px;height:132px;border-radius:50%;background:var(--white);box-shadow:0 3px 6px rgba(0,0,0,.2);text-align:center;padding-top:20px;font-size:11.5px;line-height:14px;color:#333}
  .step .n{display:block;font-size:46px;line-height:44px;font-weight:400;color:var(--green-bright);margin-bottom:4px}
  .step small{display:block;font-size:5px;line-height:6px;margin-top:3px;padding:0 16px}
  .benefit-head{top:562px;height:36px;background:var(--white);display:flex;align-items:center;justify-content:center;font-weight:700;font-size:21px;color:var(--green-bright);z-index:1}
  .benefit-head::after{content:"";position:absolute;left:50%;bottom:-9px;margin-left:-12px;border-left:12px solid transparent;border-right:12px solid transparent;border-top:9px solid var(--white)}
  .benefits-area{top:598px;height:302px;background:linear-gradient(90deg,#e1e1e3,#f3f3f4)}
  .portrait{position:absolute;right:0;top:0;width:175px;height:302px}
  .benefits{position:absolute;left:22px;top:40px;width:272px;list-style:none}
  .benefits li{border-left:3px solid var(--green-bright);padding-left:8px;font-size:12px;line-height:16px;font-weight:300;color:#1e1e1e;margin-bottom:12px}
  .benefits b{font-weight:700}
  .brand{top:900px;height:86px;padding:12px 0 0 28px;color:var(--green-bright);font-weight:400;white-space:nowrap}
  .brand .name{font-size:33px;letter-spacing:3px;line-height:38px}
  .brand .role{font-size:24px;letter-spacing:2.4px;line-height:30px}
</style>
</head>
<body>

<section class="panel panel--front">
  <h2 class="abs front-title">Vorteile bei der Arbeit mit mir</h2>
  <svg class="abs front-photos" viewBox="0 0 480 168" preserveAspectRatio="none" role="img" aria-label="Zwei Fotos: ältere Frau lächelnd im Cabrio, junge Frau mit Daumen hoch aus dem Autofenster">
    <defs>
      <linearGradient id="ph1" x1="0" y1="0" x2="1" y2="1"><stop offset="0" stop-color="#8a6b52"/><stop offset="1" stop-color="#2a2420"/></linearGradient>
      <linearGradient id="ph2" x1="0" y1="0" x2="1" y2="1"><stop offset="0" stop-color="#c9b98e"/><stop offset="1" stop-color="#8d8f93"/></linearGradient>
    </defs>
    <polygon points="0,0 243,0 216,168 0,168" fill="url(#ph1)"/>
    <polygon points="247,0 480,0 480,168 220,168" fill="url(#ph2)"/>
    <polygon points="243,0 247,0 220,168 216,168" fill="#fff"/>
  </svg>
  <div class="abs intro">Sie wollen endlich entspannt und sicher Auto fahren?<br>Panikattacken beim Autofahren überwinden?</div>
  <div class="abs cta">Dann sind Sie hier richtig!</div>
  <p class="abs question">Kommt Ihnen eine dieser Situationen bekannt vor?</p>
  <ul class="abs situations">
    <li><b>Angst oder Panikattacken</b> begleiten Sie <b>beim Autofahren.</b> Vielleicht <b>vermeiden</b> Sie deshalb das Autofahren komplett. - Sie möchten angstfrei und/oder ohne Panikattacken fahren.</li>
    <li>Sie <b>trauen sich das Autofahren nicht (mehr) zu.</b> - Sie wünschen sich, sicher, entspannt und stressfrei Auto zu fahren.</li>
    <li><b>Autofahren</b> erleben Sie unter hoher <b>Anspannung und Stress</b>. - Sie wünschen sich, Autofahren sicher und entspannt zu erleben.</li>
    <li>Bestimmte Situationen (z.B. <b>Autobahn, Baustellen, Stadtvekehr</b>...) bereiten Ihnen <b>großen Stress.</b> - Sie möchten diese Situationen souveräner meistern.</li>
  </ul>
  <h3 class="abs contact-head">CONTACT</h3>
  <div class="abs contact">
    <p>Sabine Lorenwald Weitere Informationen finden Sie auf:</p>
    <p><strong>www.fahrsicher-coaching-beispiel.de</strong></p>
    <hr>
    <p><strong>Oder rufen Sie mich einfach an:</strong></p>
    <p>Tel. <strong>0151 00 12 34 56</strong></p>
  </div>
</section>

<section class="panel panel--back">
  <div class="abs steps-band"></div>
  <svg class="abs scene" viewBox="0 0 480 438" preserveAspectRatio="none" role="img" aria-label="Foto: gelber Kleinwagen mit Koffern auf dem Dach auf einer Sommerwiese, Frau winkt aus dem Fenster">
    <defs>
      <linearGradient id="sky" x1="0" y1="0" x2="0" y2="1">
        <stop offset="0" stop-color="#6ea6de"/><stop offset=".45" stop-color="#bcd7ef"/>
        <stop offset=".55" stop-color="#4f7a30"/><stop offset=".7" stop-color="#b79a5c"/><stop offset="1" stop-color="#8a6d3c"/>
      </linearGradient>
    </defs>
    <rect width="480" height="438" fill="url(#sky)"/>
    <path d="M0,0 H480 V25 C380,60 300,10 240,20 C160,35 80,5 0,30 Z" fill="#a4d12a"/>
    <path d="M0,30 C80,5 160,35 240,20 C300,10 380,60 480,25 V40 C380,80 300,28 240,38 C160,52 80,22 0,48 Z" fill="#7cb518"/>
  </svg>
  <h2 class="steps-title"><span class="num">3</span>SCHRITTE ZUR LÖSUNG</h2>
  <div class="step" style="left:28px"><span class="n">1</span>Erstgespräch<br>vereinbaren</div>
  <div class="step" style="left:174px"><span class="n">2</span>Analyse Ihrer<br>individuellen Situation<br>und Zielsetzung</div>
  <div class="step" style="left:320px"><span class="n">3</span>Individuelles Coaching<br>und Training<small>(ggf. Therapie – als Heilpraktikerin auf Angst- und Panikstörungen spezialisiert)</small></div>
  <h3 class="abs benefit-head">VORTEILE BEI DER ARBEIT MIT MIR</h3>
  <div class="abs benefits-area">
    <svg class="portrait" viewBox="0 0 175 302" preserveAspectRatio="none" role="img" aria-label="Porträtfoto der Trainerin in weißer Bluse">
      <defs><linearGradient id="pt" x1="0" y1="0" x2="0" y2="1"><stop offset="0" stop-color="#e6e6e8"/><stop offset=".35" stop-color="#d8c2ad"/><stop offset=".55" stop-color="#f7f7f7"/><stop offset="1" stop-color="#ffffff"/></linearGradient></defs>
      <rect width="175" height="302" fill="url(#pt)"/>
    </svg>
    <ul class="benefits">
      <li>über 10 Jahre Erfahrung als <b>Trainerin</b> und Coach im Bereich <b>Fahrsicherheit.</b></li>
      <li><b>Als psychotherapeutische Heilpraktikerin</b> bin ich <b>auf Angststörungen und Panikattacken spezialisiert</b></li>
      <li><b>100 % auf Sie zugeschnitten:</b> ich hole Sie genau dort ab, wo Sie jetzt stehen und unterstütze Sie in <b>Ihrem Prozess individuell und zielführend.</b></li>
      <li>Wenn es Ihnen nicht möglich ist, in meine Praxis nach Feldbach Nord zu kommen: Mit der <b>mobilen Praxis komme ich auch zu Ihnen.</b></li>
      <li><b>Termine</b> sind auch <b>abends und am Wochenende möglich.</b></li>
    </ul>
  </div>
  <div class="abs brand">
    <div class="name">Sabine Lorenwald</div>
    <div class="role">Fahrangst-Bewältigungs-Coach</div>
  </div>
</section>

</body>
</html>
```